Meridian Lodging Partners

An Editable Business Card Template For MLP & MLH
Similar or Different Design

418 W. Harlan Brookside Pkwy.
Suite 2270
Irving, TX 75091

```html
<!DOCTYPE html>
<html lang="en">
<head>
<meta charset="utf-8">
<title>Meridian Lodging Partners – Business Card</title>
<link rel="stylesheet" href="https://fonts.googleapis.com/css2?family=Crimson+Text:wght@400;600;700&display=swap">
<style>
  :root {
    --bg: #2a2a2a;
    --card: #f1f1f1;
    --ink: #222222;
    --brand-red: #8a2329;
    --brand-red-dark: #7a1d22;
    --band-grey: #7d7f81;
    --white: #ffffff;
  }
  * { margin: 0; padding: 0; box-sizing: border-box; }
  html, body { width: 1200px; height: 1138px; overflow: hidden; background: var(--bg); }
  body { position: relative; font-family: "Crimson Text", Georgia, serif; color: var(--ink); }

  .card {
    position: absolute;
    width: 624px; height: 376px;
    background: var(--card);
    border-radius: 16px;
    overflow: hidden;
  }
  .card--front { left: 272px; top: 184px; }
  .card--back  { left: 274px; top: 606px; }

  /* Front */
  .brand-lockup {
    position: absolute; left: 0; right: 0; top: 30px;
    display: flex; align-items: center; justify-content: center; gap: 16px;
  }
  .brand-lockup__dot { width: 110px; height: 110px; border-radius: 50%; background: var(--brand-red); flex: none; }
  .brand-lockup__name { font-weight: 600; font-size: 28px; color: var(--brand-red); line-height: 1.05; }

  .office-line {
    position: absolute; left: 0; right: 0; top: 166px;
    text-align: center; font-size: 27px; line-height: 1;
  }
  .office-line__phone { color: var(--brand-red); font-weight: 700; font-size: 32px; }
  .address {
    position: absolute; left: 0; right: 0; top: 206px;
    text-align: center; font-size: 16px;
  }
  .industry-band {
    position: absolute; left: 0; right: 0; top: 242px; height: 26px;
    background: var(--band-grey); color: var(--white);
    text-align: center; font-size: 16px; line-height: 26px;
  }
  .features {
    position: absolute; left: 0; right: 0; top: 272px;
    text-align: center; font-size: 15.5px; line-height: 22px;
  }
  .features .sep { padding: 0 6px; }
  .web-band {
    position: absolute; left: 0; right: 0; bottom: 0; height: 47px;
    background: var(--brand-red); color: var(--white);
    text-align: center; font-size: 22px; line-height: 47px;
    font-variant: small-caps; letter-spacing: 0.5px;
  }

  /* Back */
  .accent-dot {
    position: absolute; left: -16px; top: 86px;
    width: 28px; height: 60px; border-radius: 0 30px 30px 0; background: var(--brand-red);
  }
  .person { position: absolute; left: 35px; top: 88px; }
  .person__name { font-size: 32px; font-weight: 700; color: var(--brand-red); line-height: 1; }
  .person__title { font-size: 20px; line-height: 1.1; margin-top: 2px; }

  .contacts { position: absolute; left: 34px; top: 222px; list-style: none; }
  .contacts li { display: flex; align-items: center; gap: 14px; font-size: 19px; height: 24px; }
  .contacts svg { width: 16px; height: 16px; fill: var(--brand-red); flex: none; }

  .brand-lockup--back {
    position: absolute; left: 330px; right: auto; top: 79px; width: 280px;
    justify-content: flex-start; gap: 14px;
  }
  .brand-lockup--back .brand-lockup__dot { width: 150px; height: 150px; }
  .brand-lockup--back .brand-lockup__name { font-size: 24px; line-height: 1.1; }

  .footer-grey {
    position: absolute; left: 0; bottom: 0; width: 230px; height: 15px; background: var(--band-grey);
  }
  .footer-tagline {
    position: absolute; right: 0; bottom: 0; width: 410px; height: 52px;
    background: var(--brand-red-dark);
    clip-path: polygon(22px 0, 100% 0, 100% 100%, 0 100%);
    color: var(--white); font-size: 23px; line-height: 52px;
    text-align: right; padding-right: 26px;
    font-variant: small-caps; letter-spacing: 0.5px;
  }
</style>
</head>
<body>

<section class="card card--front" aria-label="Business card front">
  <div class="brand-lockup">
    <span class="brand-lockup__dot"></span>
    <span class="brand-lockup__name">Meridian Lodging Partners</span>
  </div>
  <p class="office-line">Corporate Office: <span class="office-line__phone">214-555-0148</span></p>
  <p class="address">418 W. Harlan Brookside Pkwy. Suite 2270 Irving, TX 75091</p>
  <p class="industry-band">Trusted lodging partner for Oil, Gas, Energy &amp; Construction crews.</p>
  <p class="features">
    Single Monthly Invoice<span class="sep">|</span>Fully Managed Crew Lodging<span class="sep">|</span>Staffed Support Desk 24/7/365<br>
    Dependable Results On Every Job<span class="sep">|</span>Negotiated Rates &amp; Clear Pricing
  </p>
  <p class="web-band">www.MeridianLodging.com</p>
</section>

<section class="card card--back" aria-label="Business card back">
  <span class="accent-dot"></span>
  <div class="person">
    <p class="person__name">Dana Whitfield</p>
    <p class="person__title">Sales Manager</p>
  </div>
  <ul class="contacts">
    <li>
      <svg viewBox="0 0 16 16" aria-hidden="true"><path d="M1 5c0-2 3-3 7-3s7 1 7 3v1h-4V5H5v1H1zM3 7h10l1 7H2zM8 9a2 2 0 100 4 2 2 0 000-4z"/></svg>
      214-555-0148
    </li>
    <li>
      <svg viewBox="0 0 16 16" aria-hidden="true"><path d="M4 0h8a1 1 0 011 1v14a1 1 0 01-1 1H4a1 1 0 01-1-1V1a1 1 0 011-1zm1 2v10h6V2zm3 11a1 1 0 100 2 1 1 0 000-2z"/></svg>
      480-555-0163
    </li>
    <li>
      <svg viewBox="0 0 16 16" aria-hidden="true"><path d="M0 3h16v10H0zm1.5 1.2L8 9l6.5-4.8v-.2h-13zM1 12h14V5.5L8 10.5 1 5.5z"/></svg>
      dwhitfield@meridianlodging.com
    </li>
  </ul>
  <div class="brand-lockup brand-lockup--back">
    <span class="brand-lockup__dot"></span>
    <span class="brand-lockup__name">Meridian Lodging Housing</span>
  </div>
  <span class="footer-grey"></span>
  <p class="footer-tagline">Field Crew Lodging Made Simple</p>
</section>

</body>
</html>
```